Plakat-Design für Chor und Blasorchester
Zielgruppe
Konzert eines Orchesters zusammen mit drei Chören.
Zielgruppe Musikinteressierte allen Alters
(Alter der Musiker/Sänger 15-85)
Aufgabenstellung
PLakat wird in erster Linie in A3 und A4 gedruck.
Vermutlich machen wir auch Flyer

```html
<!DOCTYPE html>
<html lang="de">
<head>
<meta charset="utf-8">
<title>Ohrwürmer – Konzertplakat</title>
<link rel="stylesheet" href="https://fonts.googleapis.com/css2?family=Cinzel:wght@400;600&family=Cinzel+Decorative:wght@400&display=swap">
<style>
  :root {
    --stage: #2b2a30;
    --paper: #f1e9df;
    --paper-warm: #e6d3bf;
    --sepia: #b98e6c;
    --sepia-dark: #8a6249;
    --ink: #6a4636;
    --ink-soft: #8c6a58;
  }
  * { margin: 0; padding: 0; box-sizing: border-box; }
  html, body { width: 1200px; height: 800px; overflow: hidden; }
  body {
    background: var(--stage);
    display: flex; align-items: center; justify-content: center;
    font-family: "Cinzel", serif;
    color: var(--ink);
  }
  .poster {
    position: relative;
    width: 552px; height: 764px;
    background:
      radial-gradient(ellipse 38% 12% at 12% 73%, rgba(185,142,108,.35), transparent 70%),
      radial-gradient(ellipse 30% 14% at 92% 74%, rgba(185,142,108,.35), transparent 70%),
      radial-gradient(ellipse 60% 20% at 50% 92%, rgba(185,142,108,.18), transparent 70%),
      var(--paper);
    overflow: hidden;
    text-align: center;
  }
  .poster__portraits {
    position: absolute; left: 0; top: 0; width: 100%; height: 420px;
    background:
      radial-gradient(ellipse 30% 40% at 30% 40%, rgba(138,98,73,.55), transparent 70%),
      radial-gradient(ellipse 32% 42% at 72% 45%, rgba(138,98,73,.6), transparent 70%),
      linear-gradient(180deg, var(--paper-warm) 0%, #dcc4ae 55%, var(--paper) 100%);
  }
  .poster__title {
    position: absolute; left: 0; right: 0; top: 425px;
    font-family: "Cinzel Decorative", serif;
    font-size: 66px; font-weight: 400; letter-spacing: 1px;
    color: var(--ink); line-height: 1;
  }
  .poster__subtitle {
    position: absolute; left: 0; right: 0; top: 506px;
    font-size: 13.5px; letter-spacing: .2px; color: var(--ink-soft);
  }
  .ensemble-host {
    position: absolute; left: 0; right: 0; top: 554px;
    font-size: 10px; font-weight: 600;
  }
  .choirs {
    position: absolute; left: 28px; right: 28px; top: 584px;
    display: flex; justify-content: space-between;
  }
  .choir__name { font-size: 10px; font-weight: 600; display: block; }
  .choir__place { font-size: 6px; color: var(--ink-soft); display: block; }
  .direction { position: absolute; left: 0; right: 0; top: 620px; }
  .direction__label { font-size: 6px; color: var(--ink-soft); display: block; }
  .direction__names { font-size: 10px; font-weight: 600; display: block; }
  .concert {
    position: absolute; top: 680px; font-size: 9px; line-height: 1.35;
  }
  .concert__date { font-size: 12px; font-weight: 600; display: block; }
  .concert--first { left: 24px; text-align: left; }
  .concert--second { right: 24px; text-align: right; }
  .poster__emblem {
    position: absolute; left: 262px; top: 684px; width: 28px; height: 34px;
    background: var(--sepia); opacity: .7; border-radius: 3px;
  }
  .poster__footer {
    position: absolute; left: 24px; right: 24px; top: 740px;
    border-top: 1px solid var(--sepia);
    padding-top: 5px;
    display: flex; justify-content: space-around;
    font-size: 7.5px; letter-spacing: 6px; color: var(--ink);
  }
</style>
</head>
<body>
  <article class="poster">
    <div class="poster__portraits" role="img" aria-label="Sepia-Aquarellporträts zweier Komponisten, einer mit Bart, einer mit Hut"></div>

    <h1 class="poster__title">OHRWÜRMER</h1>
    <p class="poster__subtitle">VON VARELLI BIS CORWIN FÜR CHOR UND SINFONISCHES BLASORCHESTER</p>

    <p class="ensemble-host">MUSIKVEREIN LINDENAU (D)</p>

    <div class="choirs">
      <p class="choir"><span class="choir__name">CANTABILE CHOR</span><span class="choir__place">SEESTADT (D)</span></p>
      <p class="choir"><span class="choir__name">LE CHŒUR TALBERG</span><span class="choir__place">TALBERG (CH)</span></p>
      <p class="choir"><span class="choir__name">GEMISCHTER CHOR</span><span class="choir__place">BIRKENAU (D)</span></p>
    </div>

    <p class="direction">
      <span class="direction__label">LEITUNG</span>
      <span class="direction__names">ANKE LINDBERGER / KLAUS HOFER</span>
    </p>

    <p class="concert concert--first">
      <span class="concert__date">19. NOVEMBER 2017, 17:00 UHR</span>
      KIRCHE ST. LORENZ<br>SEESTADT
    </p>
    <div class="poster__emblem" role="img" aria-label="Kleines Ornament"></div>
    <p class="concert concert--second">
      <span class="concert__date">26. NOVEMBER 2017, 17:00 UHR</span>
      MÜHLBACH KIRCHE<br>TALBERG
    </p>

    <p class="poster__footer"><span>EINTRITT FREI</span><span>SPENDE FREUNDLICH ERBETEN</span></p>
  </article>
</body>
</html>
```